Visitenkarten-Design für virtuelle Jobmesse & Jobbörse für Soldaten
Zielgruppe
Die KLO GmbH ist ein Unternehmen das zwei Hauptprodukte betreibt! Zum einen Jobbörse für Soldaten unter www.wachwechselpunkt.de und zum anderen eine virtuelle Jobmesse für Soldaten unter www.marvento.de , die wir zweimal im Jahr veranstalten.
Aufgabenstellung
Wir haben ja die beiden Produkte Wachwechselpunkt.de und die Marvento, für die bereits jeweils ein separtes Logo besteht! Diese finden Sie im Anhang! Beide werden doch jedoch von einem Unternehmen, der KLO GmbH betrieben! Aktuell nutzen wir eine Visitenkarte mit dem Logo von KLO und eine mit dem Logo der MARVENTO. Gerade im Hinblick darauf, dass wir zukünftig auch weiter Plattformen in unser Portfolio aufnehmen, möchte ich hier unsere V-Karten flexibler gestalten!
Ziel soll es also sein, eine Visitenkarte zu gestalten, auf dem klar wird, dass der Mitarbeiter von der KLO GmbH kommt, die KLO GmbH aber unterschiedliche Produkte betreibt.
Im Anhang finden Sie:
1. Das Logo von KLO
2. Das Logo von Marvento
3. Die aktuelle V-Karte von KLO
4. Die aktuelle V-Karte von MARVENTO
Vielleicht ein kleiner Anreiz: Aktuell nutzen wir auch zwei getrennte Geschäftspapiere. Das von www.wachwechselpunkt.de lade ich einmal hoch! Der Designer, der auch die Visitenkarte erstellt, erhällt im Anschluss den 1:1 Auftrag in Höhe von 200 Euro für die Erstellung des Geschäftspapiers! Wenn Sie jetzt schon einen Vorschlag für das Geschäftspapier einreichen, erhöht das natürlich Ihre Chancen, wobei ich verspreche, dass wir im Falle eine Annahme das 1:1 im Anschluß dennoch starten werden!

```html
<!DOCTYPE html>
<html lang="de">
<head>
<meta charset="utf-8">
<title>Visitenkarten KLO GmbH</title>
<link href="https://fonts.googleapis.com/css2?family=Arimo:wght@400;700&display=swap" rel="stylesheet">
<style>
  :root {
    --stage: #cabb9e;
    --card-dark: #222222;
    --card-light: #ffffff;
    --brand-blue: #1d4b8c;
    --line-gray: #8a8a8a;
    --text-dark-muted: #5d5d5d;
    --text-light: #333333;
    --white: #ffffff;
  }
  html, body {
    margin: 0;
    padding: 0;
    width: 1200px;
    height: 1200px;
    overflow: hidden;
    background: var(--stage);
    font-family: "Arimo", Arial, sans-serif;
  }
  .canvas { position: relative; width: 1200px; height: 1200px; }
  .card {
    position: absolute;
    width: 408px;
    height: 264px;
    overflow: hidden;
    box-sizing: border-box;
  }
  .card--dark { background: var(--card-dark); }
  .card--light { background: var(--card-light); border: 1px solid #d8d8d8; }
  .card--front-dark { left: 179px; top: 300px; }
  .card--back-dark { left: 609px; top: 303px; }
  .card--front-light { left: 179px; top: 633px; }
  .card--back-light { left: 609px; top: 637px; }

  .rule { position: absolute; left: 0; width: 100%; height: 3px; }
  .rule--blue { background: var(--brand-blue); }
  .rule--gray { background: var(--line-gray); height: 2px; }

  .brand-name {
    position: absolute;
    display: flex;
    align-items: center;
    gap: 6px;
    padding: 4px 8px;
    font-weight: 700;
    letter-spacing: 0.3px;
    white-space: nowrap;
  }
  .card--dark .brand-name { background: var(--card-dark); color: #c9c9c9; }
  .card--light .brand-name { background: var(--card-light); color: #555555; }
  .brand-name__square { width: 10px; height: 10px; background: var(--brand-blue); flex: none; }
  .brand-name--small { left: 16px; top: 51px; font-size: 13px; }
  .brand-name--large { left: 50%; top: 117px; transform: translateX(-50%); font-size: 22px; padding: 6px 12px; }
  .brand-name--large .brand-name__square { width: 14px; height: 14px; }

  .company { position: absolute; left: 43px; top: 100px; font-size: 15px; font-weight: 700; }
  .card--dark .company { color: var(--text-dark-muted); }
  .card--light .company { color: #444444; }

  .person { position: absolute; left: 38px; top: 153px; }
  .person__name { font-size: 20px; color: var(--brand-blue); line-height: 1; }
  .person__role { font-size: 10px; font-weight: 700; letter-spacing: 0.5px; margin-top: 1px; }
  .card--dark .person__role { color: var(--text-dark-muted); }
  .card--light .person__role { color: #555555; }

  .contact { position: absolute; left: 211px; top: 130px; font-size: 13px; line-height: 18px; }
  .card--dark .contact { color: var(--text-dark-muted); }
  .card--light .contact { color: var(--text-light); }
  .contact__address { margin: 0 0 6px 3px; }
  .contact__row { display: flex; }
  .contact__label { color: var(--brand-blue); width: 62px; }
  .contact__row--mail { font-size: 11.5px; letter-spacing: -0.3px; }
  .contact__row--mail .contact__label { width: auto; margin-right: 3px; }

  .footer-band { position: absolute; left: 0; bottom: 0; width: 408px; height: 25px; }
  .footer-band__url {
    position: absolute; right: 30px; bottom: 5px;
    font-size: 13px; font-weight: 700; color: var(--white);
  }
</style>
</head>
<body>
<main class="canvas">

  <section class="card card--dark card--front-dark" aria-label="Vorderseite dunkel">
    <div class="rule rule--blue" style="top:60px"></div>
    <div class="rule rule--gray" style="top:65px"></div>
    <div class="brand-name brand-name--small"><span class="brand-name__square"></span>Wachwechselpunkt</div>
    <div class="company">KLO GmbH</div>
    <div class="person">
      <div class="person__name">Jonas Berger</div>
      <div class="person__role">Geschäftsführer</div>
    </div>
    <div class="contact">
      <div class="contact__address">Lindenweg 14<br>86650 Halsdorf</div>
      <div class="contact__row"><span class="contact__label">Telefon.:</span>08431 - 552 17 30</div>
      <div class="contact__row"><span class="contact__label">Mobil.:</span>0171 - 384 92 517</div>
      <div class="contact__row contact__row--mail"><span class="contact__label">E.:</span>jonas.berger@wachwechselpunkt.de</div>
    </div>
    <svg class="footer-band" viewBox="0 0 408 25" aria-hidden="true">
      <defs>
        <linearGradient id="steelDark" x1="0" x2="1" y1="0" y2="0">
          <stop offset="0" stop-color="#5a5a5a"/>
          <stop offset="0.45" stop-color="#9a9a9a"/>
          <stop offset="1" stop-color="#2a2a2a"/>
        </linearGradient>
      </defs>
      <polygon points="0,0 158,0 150,25 0,25" fill="url(#steelDark)"/>
      <polygon points="162,0 168,0 160,25 154,25" fill="#6e6e6e"/>
      <polygon points="172,0 178,0 170,25 164,25" fill="#6e6e6e"/>
      <polygon points="182,0 188,0 180,25 174,25" fill="#6e6e6e"/>
      <polygon points="200,0 408,0 408,25 192,25" fill="#1d4b8c"/>
    </svg>
    <div class="footer-band__url">www.wachwechselpunkt.de</div>
  </section>

  <section class="card card--dark card--back-dark" aria-label="Rückseite dunkel">
    <div class="rule rule--blue" style="top:128px"></div>
    <div class="rule rule--gray" style="top:134px"></div>
    <div class="brand-name brand-name--large"><span class="brand-name__square"></span>Wachwechselpunkt</div>
  </section>

  <section class="card card--light card--front-light" aria-label="Vorderseite hell">
    <div class="rule rule--blue" style="top:60px"></div>
    <div class="rule rule--gray" style="top:65px"></div>
    <div class="brand-name brand-name--small"><span class="brand-name__square"></span>Wachwechselpunkt</div>
    <div class="company">KLO GmbH</div>
    <div class="person">
      <div class="person__name">Jonas Berger</div>
      <div class="person__role">Geschäftsführer</div>
    </div>
    <div class="contact">
      <div class="contact__address">Lindenweg 14<br>86650 Halsdorf</div>
      <div class="contact__row"><span class="contact__label">Telefon.:</span>08431 - 552 17 30</div>
      <div class="contact__row"><span class="contact__label">Mobil.:</span>0171 - 384 92 517</div>
      <div class="contact__row contact__row--mail"><span class="contact__label">E.:</span>jonas.berger@wachwechselpunkt.de</div>
    </div>
    <svg class="footer-band" viewBox="0 0 408 25" aria-hidden="true">
      <defs>
        <linearGradient id="steelLight" x1="0" x2="1" y1="0" y2="0">
          <stop offset="0" stop-color="#8c8c8c"/>
          <stop offset="0.5" stop-color="#5a5a5a"/>
          <stop offset="1" stop-color="#1e1e1e"/>
        </linearGradient>
      </defs>
      <polygon points="0,0 158,0 150,25 0,25" fill="url(#steelLight)"/>
      <polygon points="162,0 168,0 160,25 154,25" fill="#444444"/>
      <polygon points="172,0 178,0 170,25 164,25" fill="#444444"/>
      <polygon points="182,0 188,0 180,25 174,25" fill="#444444"/>
      <polygon points="200,0 408,0 408,25 192,25" fill="#1d4b8c"/>
    </svg>
    <div class="footer-band__url">www.wachwechselpunkt.de</div>
  </section>

  <section class="card card--light card--back-light" aria-label="Rückseite hell">
    <div class="rule rule--blue" style="top:128px"></div>
    <div class="rule rule--gray" style="top:134px"></div>
    <div class="brand-name brand-name--large"><span class="brand-name__square"></span>Wachwechselpunkt</div>
  </section>

</main>
</body>
</html>
```